Company Gift Card Designs

I would like to have 2 gift cards designed.

Both cards need to be in our company colors and have a non-white background. Both will need to follow the attached spec sheet from the card vendor.

Card 1 - will need to have the words Thank you on the card and use the Norvale Logo

Card 2 - will need to have both the Norvale logo and the Brightway Logo incorporated into the design.

```html
<!DOCTYPE html>
<html lang="en">
<head>
<meta charset="utf-8">
<title>Norvale Gift Cards</title>
<link href="https://fonts.googleapis.com/css2?family=Barlow:wght@700;800&display=swap" rel="stylesheet">
<style>
  :root {
    --stage: #9a9695;
    --card-dark: #434445;
    --brand-red: #c01f26;
    --brand-blue: #2e8ec4;
    --ink: #1f1f20;
    --white: #ffffff;
    --label: #bdbab9;
    --guide: #2a2a2a;
  }
  html, body {
    margin: 0;
    padding: 0;
    width: 1200px;
    height: 456px;
    overflow: hidden;
    background: var(--stage);
    font-family: "Barlow", Arial, sans-serif;
  }
  .stage { position: relative; width: 1200px; height: 456px; }

  .card {
    position: absolute;
    top: 44px;
    width: 511px;
    height: 327px;
    background: var(--card-dark);
    overflow: hidden;
    box-shadow: 8px 10px 12px rgba(0,0,0,0.35);
  }
  .card--one { left: 56px; }
  .card--two { left: 632px; }

  .card__footer {
    position: absolute;
    left: 0; right: 0; bottom: 0;
    height: 67px;
    background: var(--white);
  }

  .card__safe-line {
    position: absolute;
    inset: 6px;
    border: 1px dashed var(--guide);
    border-radius: 6px;
    pointer-events: none;
    z-index: 5;
  }

  .thank-you {
    position: absolute;
    left: 0;
    margin: 0;
    font-weight: 800;
    font-size: 58px;
    letter-spacing: 4px;
    line-height: 1;
    color: var(--brand-blue);
    -webkit-text-stroke: 5px var(--white);
    paint-order: stroke fill;
    text-shadow: 2px 3px 4px rgba(0,0,0,0.45);
    text-align: center;
    white-space: nowrap;
  }
  .card--one .thank-you { width: 487px; top: 112px; }
  .card--two .thank-you { width: 511px; top: 131px; }

  .amount {
    position: absolute;
    background: var(--brand-red);
    color: var(--white);
    font-weight: 800;
    font-size: 64px;
    line-height: 1;
    display: flex;
    align-items: center;
    justify-content: center;
    box-shadow: 2px 3px 5px rgba(0,0,0,0.4);
  }

  .card--one .red-strip {
    position: absolute;
    top: 0; bottom: 0; right: 0;
    width: 25px;
    background: var(--brand-red);
    box-shadow: -2px 0 4px rgba(0,0,0,0.35);
  }
  .card--one .amount {
    left: 329px;
    top: 228px;
    width: 158px;
    height: 82px;
    border-radius: 5px 0 0 5px;
  }

  .card--two .red-band {
    position: absolute;
    top: 0; left: 0; right: 0;
    height: 28px;
    background: var(--brand-red);
    box-shadow: 0 2px 4px rgba(0,0,0,0.35);
  }
  .card--two .amount {
    left: 171px;
    top: 20px;
    width: 170px;
    height: 77px;
    border-radius: 0 0 5px 5px;
  }

  .brand-name {
    position: absolute;
    bottom: 18px;
    font-weight: 800;
    line-height: 1;
    white-space: nowrap;
  }
  .brand-name--main { left: 16px; font-size: 32px; color: var(--brand-blue); }
  .brand-name--partner { right: 18px; font-size: 30px; color: var(--ink); }

  .card-label {
    position: absolute;
    top: 411px;
    margin: 0;
    font-weight: 800;
    font-size: 22px;
    letter-spacing: 2px;
    color: var(--label);
    line-height: 1;
  }
  .card-label--one { left: 257px; }
  .card-label--two { left: 873px; }
</style>
</head>
<body>
<main class="stage">

  <section class="card card--one" aria-label="Gift card one">
    <div class="card__footer"></div>
    <div class="red-strip"></div>
    <h2 class="thank-you">THANK YOU</h2>
    <div class="amount">$500</div>
    <span class="brand-name brand-name--main">Norvale</span>
    <div class="card__safe-line"></div>
  </section>

  <section class="card card--two" aria-label="Gift card two">
    <div class="card__footer"></div>
    <div class="red-band"></div>
    <div class="amount">$500</div>
    <h2 class="thank-you">THANK YOU</h2>
    <span class="brand-name brand-name--main">Norvale</span>
    <span class="brand-name brand-name--partner">Brightway</span>
    <div class="card__safe-line"></div>
  </section>

  <p class="card-label card-label--one">CARD 1</p>
  <p class="card-label card-label--two">CARD 2</p>

</main>
</body>
</html>
```